(4) Bowling League Designs 1920x1080

Will be used on our website and in some digital signage.

We are starting (4) leagues this summer and need a basic graphic as an attention grab which will then lead the customer to full information / sign ups. The information I would need on each one is as follows:

1. Monday Night FREE ball league - Begins May 3rd

2. Tuesday Trios - NPTA Sanctioned - Begins May 11th
$9,000 prize fund

3. Wednesday Cosmic League - 9 pin no tap fun league - May 12th start

4. Thursday Night FREE ball league - Begins May 13th

I will attach some random examples of previous ones to give you an idea.

```html
<!DOCTYPE html>
<html lang="en">
<head>
<meta charset="utf-8">
<title>Monday Night Free Ball League</title>
<link href="https://fonts.googleapis.com/css2?family=Graduate&family=Roboto+Slab:wght@400;600;800&display=swap" rel="stylesheet">
<style>
  :root {
    --page: #e4e4e4;
    --navy-deep: #0b2454;
    --navy: #12357a;
    --blue-bright: #1f52a8;
    --sky: #5b9be0;
    --sky-light: #7fb4ec;
    --orange: #f6a21e;
    --white: #ffffff;
    --silver-light: #eef0f3;
    --silver-mid: #a9aeb6;
    --silver-dark: #6d727b;
    --art-light: #eceff3;
    --art-mid: #c4c9d1;
    --art-red: #a51c26;
  }
  * { margin: 0; padding: 0; box-sizing: border-box; }
  html, body { width: 1200px; height: 796px; overflow: hidden; }
  body { background: var(--page); position: relative; }

  .banner {
    position: absolute;
    left: 72px; top: 101px;
    width: 1056px; height: 594px;
    overflow: hidden;
    background:
      radial-gradient(ellipse 70% 80% at 80% 20%, var(--blue-bright) 0%, transparent 70%),
      linear-gradient(135deg, var(--navy-deep) 0%, var(--navy) 55%, var(--navy-deep) 100%);
  }

  .halftone-glow {
    position: absolute;
    right: 0; top: 0;
    width: 320px; height: 270px;
    background: radial-gradient(ellipse at 90% 10%, rgba(246,162,30,.6) 0%, rgba(246,162,30,.2) 40%, transparent 70%);
  }

  .lane-strokes { position: absolute; inset: 0; }

  .bowling-art {
    position: absolute;
    left: 740px; top: 120px;
    width: 300px; height: 400px;
    border-radius: 28px;
    background: linear-gradient(165deg, var(--art-light) 0%, var(--art-mid) 50%, var(--art-red) 100%);
    opacity: .9;
  }

  .headline {
    position: absolute;
    left: 70px; top: 70px;
    width: 640px; height: 420px;
    transform: rotate(-10deg);
    transform-origin: 50% 50%;
  }

  .speed-lines { position: absolute; inset: 0; overflow: visible; }

  .title-day {
    position: absolute;
    left: 0; top: 0;
    font-family: "Graduate", "Arial Black", sans-serif;
    font-size: 118px;
    font-weight: 400;
    line-height: 1;
    letter-spacing: -2px;
    white-space: nowrap;
    background: linear-gradient(180deg, var(--silver-light) 0%, var(--silver-mid) 48%, var(--silver-dark) 52%, var(--silver-light) 100%);
    -webkit-background-clip: text;
    background-clip: text;
    color: transparent;
    filter: drop-shadow(3px 4px 0 rgba(0,0,0,.45));
  }

  .title-night {
    position: absolute;
    left: 110px; top: 124px;
    padding: 6px 26px 8px;
    background: var(--orange);
    font-family: "Graduate", "Arial Black", sans-serif;
    font-size: 108px;
    line-height: 1;
    color: var(--navy-deep);
    white-space: nowrap;
  }

  .league-name {
    position: absolute;
    left: 20px; top: 268px;
    font-family: "Roboto Slab", serif;
    font-size: 56px;
    line-height: 1;
    color: var(--white);
    font-weight: 400;
    letter-spacing: 1px;
    white-space: nowrap;
  }
  .league-name .free { color: var(--orange); font-weight: 800; margin-right: 14px; }

  .start-date {
    position: absolute;
    left: 80px; top: 344px;
    display: flex; align-items: center; gap: 16px;
    font-family: "Roboto Slab", serif;
    font-weight: 600;
    font-size: 28px;
    letter-spacing: 3px;
    color: var(--white);
    white-space: nowrap;
  }
  .start-date::before,
  .start-date::after {
    content: "";
    display: block;
    width: 56px; height: 3px;
    background: var(--white);
  }
</style>
</head>
<body>
  <main class="banner">
    <div class="halftone-glow" role="img" aria-label="Orange halftone dot texture"></div>

    <svg class="lane-strokes" viewBox="0 0 1056 594" preserveAspectRatio="none" aria-hidden="true">
      <polygon points="380,594 760,500 1056,430 1056,462 790,535 560,594" fill="var(--orange)"/>
      <polygon points="560,594 780,520 1056,420 1056,594" fill="var(--sky)"/>
      <polygon points="700,594 900,530 1056,490 1056,594" fill="var(--sky-light)"/>
    </svg>

    <div class="bowling-art" role="img" aria-label="Red bowling ball striking three white bowling pins with red stripes"></div>

    <div class="headline">
      <svg class="speed-lines" viewBox="0 0 640 420" aria-hidden="true">
        <g stroke="var(--white)" stroke-width="4" stroke-linecap="round">
          <line x1="545" y1="140" x2="680" y2="140"/>
          <line x1="560" y1="172" x2="660" y2="172"/>
          <line x1="545" y1="210" x2="700" y2="210"/>
          <line x1="590" y1="262" x2="720" y2="262"/>
          <line x1="-10" y1="190" x2="100" y2="190"/>
          <line x1="10" y1="226" x2="100" y2="226"/>
          <line x1="-20" y1="258" x2="80" y2="258"/>
        </g>
      </svg>

      <h1 class="title-day">MONDAY</h1>
      <div class="title-night">NIGHT</div>
      <p class="league-name"><span class="free">FREE</span>BALL LEAGUE</p>
      <p class="start-date">BEGINS MAY 3RD</p>
    </div>
  </main>
</body>
</html>
```